Numbrella : This is a Puzzle and This is not a Puzzle

Numbrella is a new addictive way to play Sudoku (see description on the attached document).
We would like your help in developing a design for the playscreen of the game (a mock-up is in the attached document)
The winner will be entrusted with the work of the complete design of the application (home screen, configuration screen, etc.) in a specific contract.
Thank you from Paris France.
Best.
Anselme

```html
<!DOCTYPE html>
<html lang="en">
<head>
<meta charset="utf-8">
<title>Numbrella : This is a Puzzle and This is not a Puzzle</title>
<link rel="stylesheet" href="https://fonts.googleapis.com/css2?family=Baloo+2:wght@500;600;700&display=swap">
<style>
  :root{
    --maroon:#6a1524;
    --gold:#f1b416;
    --ink:#1c1c1c;
    --white:#ffffff;
    --black:#000000;
    --c-blue:#0a14c8;
    --c-cyan:#00f5f5;
    --c-gold:#c9970e;
    --c-red:#e50a0a;
    --c-silver:#c3c3c3;
    --c-magenta:#f012f0;
    --c-yellow:#ffff00;
    --c-green:#22f022;
    --c-orange:#ffa800;
  }
  *{box-sizing:border-box;margin:0;padding:0}
  html,body{width:1200px;height:599px;overflow:hidden}
  body{background:var(--maroon);font-family:"Baloo 2",sans-serif;position:relative;color:var(--ink)}

  .brand{position:absolute;left:25px;top:44px;display:flex;align-items:center;gap:10px;color:var(--gold);font-size:27px;font-weight:600}
  .brand-mark{width:28px;height:28px;border:3px solid var(--gold);border-radius:4px}

  .rating{position:absolute;left:18px;width:177px;height:54px;border:3px solid var(--gold);border-radius:14px;display:flex;align-items:center;gap:12px;padding-left:12px}
  .rating-icon{width:34px;height:34px;border:3px solid var(--gold);border-radius:8px;display:flex;align-items:center;justify-content:center}
  .stars{font-size:22px;letter-spacing:1px;color:var(--gold)}
  .stars .off{color:#e9b7c0}
  .rating.player{top:118px}
  .rating.level{top:188px}

  .tool-panel{position:absolute;top:254px;width:182px;height:319px;border:2px solid var(--gold);display:flex;flex-direction:column}
  .tool-panel.left{left:15px}
  .tool-panel.right{left:1014px}
  .tool{flex:1;display:flex;align-items:center;justify-content:center;border-bottom:2px solid var(--gold)}
  .tool:last-child{border-bottom:none}

  .nav-panel{position:absolute;left:1014px;top:28px;width:182px;height:160px;border:2px solid var(--gold);display:flex;flex-direction:column}
  .nav-panel .tool{gap:12px;color:var(--gold);font-size:22px;font-weight:700}

  .legend{position:absolute;top:38px;display:flex;flex-direction:column}
  .legend-row{height:58px;display:flex;align-items:center}
  .count{width:27px;height:26px;background:var(--black);color:var(--white);font-size:17px;font-weight:600;display:flex;align-items:center;justify-content:center;line-height:1}
  .legend.colours{left:237px}
  .legend.colours .count{margin-right:9px}
  .swatch{width:54px;height:58px}
  .legend.digits{left:879px}
  .legend.digits .digit{width:54px;height:55px;background:var(--white);color:var(--ink);font-size:24px;font-weight:600;display:flex;align-items:center;justify-content:center;margin:1.5px 0}
  .legend.digits .count{margin-left:9px}

  .board{position:absolute;left:345px;top:37px;display:grid;
    grid-template-columns:54px 54px 60px 54px 54px 60px 54px 54px 54px;
    grid-template-rows:54px 54px 60px 54px 54px 60px 54px 54px 54px;
    gap:2px}
  .cell{width:54px;height:54px;display:flex;align-items:center;justify-content:center;font-size:34px;font-weight:600;line-height:1;padding-top:4px}
  .bl{background:var(--c-blue);color:var(--white)}
  .cy{background:var(--c-cyan)}
  .go{background:var(--c-gold)}
  .re{background:var(--c-red)}
  .si{background:var(--c-silver)}
  .bk{background:var(--black);color:var(--white)}
  .ma{background:var(--c-magenta)}
  .ye{background:var(--c-yellow)}
  .gr{background:var(--c-green)}
  .or{background:var(--c-orange)}
</style>
</head>
<body>

<div class="brand"><span class="brand-mark"></span>Numbrella</div>

<div class="rating player">
  <span class="rating-icon">
    <svg width="22" height="22" viewBox="0 0 22 22" fill="none" stroke="#f1b416" stroke-width="2.5"><circle cx="11" cy="11" r="9"/><circle cx="11" cy="9" r="3"/><path d="M5.5 17.5c1.5-3 9.5-3 11 0"/></svg>
  </span>
  <span class="stars">★★★<span class="off">★★</span></span>
</div>
<div class="rating level">
  <span class="rating-icon">
    <svg width="20" height="20" viewBox="0 0 20 20" fill="#f1b416"><rect x="1" y="1" width="5" height="5"/><rect x="7.5" y="1" width="5" height="5"/><rect x="14" y="1" width="5" height="5"/><rect x="1" y="7.5" width="5" height="5"/><rect x="7.5" y="7.5" width="5" height="5"/><rect x="14" y="7.5" width="5" height="5"/><rect x="1" y="14" width="5" height="5"/><rect x="7.5" y="14" width="5" height="5"/><rect x="14" y="14" width="5" height="5"/></svg>
  </span>
  <span class="stars">★★★★<span class="off">★</span></span>
</div>

<div class="tool-panel left">
  <div class="tool"><svg width="48" height="34" viewBox="0 0 48 34" fill="#f1b416"><path d="M24 2 2 17l22 15z"/><path d="M46 2 24 17l22 15z"/></svg></div>
  <div class="tool"><svg width="42" height="46" viewBox="0 0 42 46"><g fill="#f1b416"><rect x="2" y="2" width="10" height="10"/><rect x="16" y="2" width="10" height="10"/><rect x="30" y="2" width="10" height="10"/><rect x="2" y="16" width="10" height="10"/><rect x="16" y="16" width="10" height="10"/><rect x="30" y="16" width="10" height="10"/><rect x="2" y="30" width="10" height="10"/><rect x="16" y="30" width="10" height="10"/><rect x="30" y="30" width="10" height="10"/></g><rect x="8" y="42" width="26" height="3" fill="#f1b416"/></svg></div>
  <div class="tool"><svg width="46" height="40" viewBox="0 0 46 40"><g transform="rotate(-35 23 20)"><rect x="4" y="12" width="38" height="17" rx="3" fill="#f1b416"/><rect x="4" y="12" width="15" height="17" rx="3" fill="#ffffff"/></g></svg></div>
  <div class="tool"><svg width="36" height="44" viewBox="0 0 36 44" fill="none" stroke="#f1b416" stroke-width="3"><path d="M18 3a13 13 0 0 0-8 23c2 2 3 4 3 7h10c0-3 1-5 3-7A13 13 0 0 0 18 3z"/><path d="M13 37h10M14 41h8"/></svg></div>
</div>

<div class="nav-panel">
  <div class="tool"><svg width="36" height="32" viewBox="0 0 36 32" fill="#f1b416"><path d="M18 2 2 16h5v14h8v-9h6v9h8V16h5z"/></svg>Home</div>
  <div class="tool"><svg width="38" height="42" viewBox="0 0 38 42" fill="none" stroke="#f1b416" stroke-width="3.5"><circle cx="19" cy="24" r="15"/><path d="M14 4h10M19 4v5M19 24V16M19 24l6 4"/></svg></div>
</div>

<div class="tool-panel right">
  <div class="tool"><svg width="48" height="34" viewBox="0 0 48 34" fill="#f1b416"><path d="M2 2l22 15L2 32z"/><path d="M24 2l22 15-22 15z"/></svg></div>
  <div class="tool"><svg width="48" height="48" viewBox="0 0 48 48" fill="none" stroke="#f1b416" stroke-width="2.5"><rect x="3" y="3" width="36" height="36"/><path d="M15 3v36M27 3v36M3 15h36M3 27h36"/><path d="M40 22l5 4-12 18-5 1 1-5z" fill="#6a1524"/><text x="7" y="13" fill="#f1b416" stroke="none" font-size="9" font-family="Baloo 2, sans-serif">1</text><text x="18" y="13" fill="#f1b416" stroke="none" font-size="9" font-family="Baloo 2, sans-serif">3</text><text x="18" y="25" fill="#f1b416" stroke="none" font-size="9" font-family="Baloo 2, sans-serif">2</text></svg></div>
  <div class="tool"><svg width="50" height="40" viewBox="0 0 50 40"><g transform="rotate(-35 25 20)"><rect x="6" y="11" width="40" height="18" rx="3" fill="#ffffff" stroke="#f1b416" stroke-width="3"/><rect x="6" y="11" width="16" height="18" rx="3" fill="#f1b416"/></g></svg></div>
  <div class="tool"><svg width="44" height="48" viewBox="0 0 44 48" fill="none" stroke="#f1b416" stroke-width="3"><path d="M22 8a12 12 0 0 0-7 21c2 2 3 3 3 6h8c0-3 1-4 3-6A12 12 0 0 0 22 8z" fill="#f1b416"/><path d="M18 40h8M19 44h6M22 1v3M6 7l3 3M38 7l-3 3M2 21h4M38 21h4"/></svg></div>
</div>

<div class="legend colours">
  <div class="legend-row"><span class="count">5</span><span class="swatch ye"></span></div>
  <div class="legend-row"><span class="count">3</span><span class="swatch ma"></span></div>
  <div class="legend-row"><span class="count">7</span><span class="swatch go"></span></div>
  <div class="legend-row"><span class="count">4</span><span class="swatch re"></span></div>
  <div class="legend-row"><span class="count">6</span><span class="swatch or"></span></div>
  <div class="legend-row"><span class="count">5</span><span class="swatch bl"></span></div>
  <div class="legend-row"><span class="count">4</span><span class="swatch gr"></span></div>
  <div class="legend-row"><span class="count">8</span><span class="swatch cy"></span></div>
  <div class="legend-row"><span class="count">2</span><span class="swatch bk"></span></div>
</div>

<div class="board">
  <div class="cell ye">5</div><div class="cell ma">3</div><div class="cell cy">8</div><div class="cell bl">1</div><div class="cell si">9</div><div class="cell bk">6</div><div class="cell gr">2</div><div class="cell re">7</div><div class="cell go">4</div>
  <div class="cell bl">1</div><div class="cell si">9</div><div class="cell bk">6</div><div class="cell gr">2</div><div class="cell re">7</div><div class="cell go">4</div><div class="cell ma">5</div><div class="cell cy">3</div><div class="cell ye">8</div>
  <div class="cell gr">2</div><div class="cell re">7</div><div class="cell go">4</div><div class="cell ma">5</div><div class="cell cy">3</div><div class="cell ye">8</div><div class="cell si">1</div><div class="cell bk">9</div><div class="cell bl">6</div>
  <div class="cell ma">3</div><div class="cell cy">8</div><div class="cell ye">1</div><div class="cell si">9</div><div class="cell bk">6</div><div class="cell bl">2</div><div class="cell re">7</div><div class="cell go">4</div><div class="cell gr">5</div>
  <div class="cell si">9</div><div class="cell bk">6</div><div class="cell bl">2</div><div class="cell re">7</div><div class="cell go">4</div><div class="cell gr">5</div><div class="cell cy">3</div><div class="cell ye">8</div><div class="cell ma">1</div>
  <div class="cell re">7</div><div class="cell go">4</div><div class="cell gr">5</div><div class="cell cy">3</div><div class="cell ye">8</div><div class="cell ma">1</div><div class="cell bk">9</div><div class="cell bl">6</div><div class="cell si">2</div>
  <div class="cell cy">8</div><div class="cell ye">1</div><div class="cell ma">9</div><div class="cell bk">6</div><div class="cell bl">2</div><div class="cell si">7</div><div class="cell go">4</div><div class="cell gr">5</div><div class="cell re">3</div>
  <div class="cell bk">6</div><div class="cell bl">2</div><div class="cell si">7</div><div class="cell go">4</div><div class="cell gr">5</div><div class="cell re">3</div><div class="cell ye">8</div><div class="cell ma">1</div><div class="cell cy">9</div>
  <div class="cell go">4</div><div class="cell gr">5</div><div class="cell re">3</div><div class="cell ye">8</div><div class="cell ma">1</div><div class="cell cy">9</div><div class="cell bl">6</div><div class="cell si">2</div><div class="cell bk">7</div>
</div>

<div class="legend digits">
  <div class="legend-row"><span class="digit">1</span><span class="count">5</span></div>
  <div class="legend-row"><span class="digit">2</span><span class="count">3</span></div>
  <div class="legend-row"><span class="digit">3</span><span class="count">7</span></div>
  <div class="legend-row"><span class="digit">4</span><span class="count">4</span></div>
  <div class="legend-row"><span class="digit">5</span><span class="count">6</span></div>
  <div class="legend-row"><span class="digit">6</span><span class="count">5</span></div>
  <div class="legend-row"><span class="digit">7</span><span class="count">4</span></div>
  <div class="legend-row"><span class="digit">8</span><span class="count">8</span></div>
  <div class="legend-row"><span class="digit">9</span><span class="count">2</span></div>
</div>

</body>
</html>
```